Business Card Design

We are a cutting edge natural health care provider who specializes in neuro behavioral conditions. We use brain mapping, neurofeedback, functional neurology and functional medicine to help people achieve their health goals.
We need a business card design for a new office. Would like to position ourselves as an upscale/concierge level treatment center that provides hope and results to people with chronic conditions. We would like the card to feature a brain, possibly a die cut shape. Design needs to communicate our tag line of "providing excellent care for difficult cases."
On back side of card:
By retraining abnormal brainwave patterns and eliminating metabolic problems, our programs often improve symptoms of:
ADD/ADHD
Addiction
Anxiety
Autism
Depression
Fibromyalgia
Insomnia
Memory Loss
Sensory/Motor Dysfunction

Target Market(s)

30-60 year olds with chronic conditions (Anxiety, depression,) or parents of children with chronic conditions (ADHD, autism, learning disorders, etc)

Industry/Entity Type

Health

Contact Information for Business Card

The Halvey Clinic
Dr. Colin Halvey, DC
2641 Orchard Pkwy. Suite 207
Duluth, GA 30097
(770) 555-0148
Fax (770) 555-0193
www.TheHalveyClinic.example
www.DrColinHalvey.example

Requirements
Nice to have
• Picture of a brain that really pops on the page.

```html
<!DOCTYPE html>
<html lang="en">
<head>
<meta charset="utf-8">
<title>The Halvey Clinic — Business Card</title>
<link href="https://fonts.googleapis.com/css2?family=Open+Sans:wght@400;600;700&display=swap" rel="stylesheet">
<style>
  :root {
    --backdrop: #2e2420;
    --card: #eeeee8;
    --ink: #151515;
    --brand-ink: #3f3f3f;
    --head-navy: #0d3a5c;
    --arrow: #555555;
    --paper: #e4e2dc;
  }
  * { margin: 0; padding: 0; box-sizing: border-box; }
  html, body {
    width: 1200px; height: 750px; overflow: hidden;
    background: var(--backdrop);
    font-family: "Open Sans", Arial, sans-serif;
    color: var(--ink);
  }
  .card {
    position: absolute; left: 75px; top: 75px;
    width: 1050px; height: 600px;
    background: var(--card);
  }
  .card-art { position: absolute; inset: 0; }
  .paper-note { fill: var(--paper); }
  .hint-arrow { fill: none; stroke: var(--arrow); stroke-width: 2.2; stroke-linecap: round; stroke-linejoin: round; }
  .head-illustration {
    position: absolute; left: 175px; top: 150px;
    width: 180px; height: 200px;
    background: var(--head-navy);
    border-radius: 60px 70px 30px 40px;
  }
  .condition {
    position: absolute; font-size: 19px; font-weight: 400; white-space: nowrap;
  }
  .condition--adhd { left: 105px; top: 70px; transform: rotate(-40deg); transform-origin: left bottom; }
  .condition--anxiety { left: 470px; top: 215px; }
  .condition--depression { left: 435px; top: 320px; }
  .condition--autism { left: 120px; top: 385px; transform: rotate(-22deg); transform-origin: left bottom; }
  .doctor-name {
    position: absolute; right: 80px; top: 38px;
    font-size: 42px; font-weight: 600; letter-spacing: -0.3px;
  }
  .primary-site {
    position: absolute; left: 660px; top: 185px;
    font-size: 20px; font-weight: 400;
  }
  .contact-list {
    position: absolute; left: 715px; top: 245px;
    list-style: none; font-size: 17px; line-height: 1.25;
  }
  .contact-list li { display: flex; align-items: flex-start; gap: 16px; margin-bottom: 10px; }
  .contact-icon { width: 20px; height: 20px; flex: none; fill: var(--ink); }
  .brand-name {
    position: absolute; left: 160px; top: 470px;
    font-size: 46px; font-weight: 700; letter-spacing: -1.2px;
    color: var(--brand-ink);
  }
</style>
</head>
<body>
  <article class="card">
    <svg class="card-art" width="1050" height="600" viewBox="0 0 1050 600" aria-hidden="true">
      <rect class="paper-note" x="175" y="80" width="60" height="60" transform="rotate(-8 205 110)"/>
      <rect class="paper-note" x="385" y="190" width="65" height="65" transform="rotate(10 417 222)"/>
      <rect class="paper-note" x="375" y="285" width="65" height="65" transform="rotate(-6 407 317)"/>
      <rect class="paper-note" x="150" y="320" width="60" height="60" transform="rotate(6 180 350)"/>
      <path class="hint-arrow" d="M180 110 C 215 105, 230 130, 222 162"/>
      <path class="hint-arrow" d="M212 152 L222 164 L232 150"/>
      <path class="hint-arrow" d="M455 230 C 430 245, 400 248, 380 238"/>
      <path class="hint-arrow" d="M392 230 L379 238 L393 246"/>
      <path class="hint-arrow" d="M420 330 C 395 330, 375 315, 368 295"/>
      <path class="hint-arrow" d="M364 308 L368 294 L378 305"/>
      <path class="hint-arrow" d="M165 385 C 160 355, 180 335, 208 330"/>
      <path class="hint-arrow" d="M196 324 L209 330 L198 339"/>
    </svg>

    <div class="head-illustration" role="img" aria-label="Navy head silhouette in profile with thought bubbles rising from the top"></div>

    <span class="condition condition--adhd">ADD/ADHD</span>
    <span class="condition condition--anxiety">Anxiety</span>
    <span class="condition condition--depression">Depression</span>
    <span class="condition condition--autism">Autism</span>

    <h1 class="doctor-name">Dr. Colin Halvey</h1>
    <p class="primary-site">www.TheHalveyClinic.example</p>

    <ul class="contact-list">
      <li>
        <svg class="contact-icon" viewBox="0 0 20 20" aria-hidden="true"><circle cx="10" cy="10" r="9"/><path d="M7 5 l2 2 -1 2 c1 2 2 3 3 3 l2 -1 2 2 -2 2 c-4 0 -8 -4 -8 -8z" fill="#eeeee8"/></svg>
        <span>(770) 555-0148</span>
      </li>
      <li>
        <svg class="contact-icon" viewBox="0 0 20 20" aria-hidden="true"><rect x="5" y="2" width="10" height="5"/><rect x="1" y="7" width="18" height="8" rx="1"/><rect x="5" y="12" width="10" height="6" fill="#eeeee8" stroke="#151515" stroke-width="1.5"/></svg>
        <span>(770) 555-0193</span>
      </li>
      <li>
        <svg class="contact-icon" viewBox="0 0 20 20" aria-hidden="true"><g fill="none" stroke="#151515" stroke-width="1.6"><circle cx="10" cy="10" r="8"/><ellipse cx="10" cy="10" rx="3.5" ry="8"/><path d="M2 10h16M3.5 6h13M3.5 14h13"/></g></svg>
        <span>www.TheHalveyClinic.example</span>
      </li>
      <li>
        <svg class="contact-icon" viewBox="0 0 20 20" aria-hidden="true"><g fill="none" stroke="#151515" stroke-width="1.6"><circle cx="10" cy="10" r="8"/><ellipse cx="10" cy="10" rx="3.5" ry="8"/><path d="M2 10h16M3.5 6h13M3.5 14h13"/></g></svg>
        <span>www.DrColinHalvey.example</span>
      </li>
      <li>
        <svg class="contact-icon" viewBox="0 0 20 20" aria-hidden="true"><path d="M10 2 L19 10 H16 V18 H12 V13 H8 V18 H4 V10 H1 Z"/></svg>
        <span>DC 2641 Orchard Pkwy.<br>Suite 207 Duluth, GA 30097</span>
      </li>
    </ul>

    <p class="brand-name">The Halvey Clinic</p>
  </article>
</body>
</html>
```